Downloadable PDF "Brochure?"

We have a Free download we will provide in exchange for an email address on our new Trailcrest website. The website at www.venturetrailcrest-example.com is in development and will look nothing like what it currently does, but you can go there and get a sense of what Trailcrest is from the text on the website. (see the attached image 'site design' for the new redesigned website for aesthetics).

We are looking for a nice design for the document, that will represent the mostly text document well. We are not actually looking to print these at a printer so they don't have to be print ready. I went ahead and included the logo and colors and fonts file again just for reference.

Target Market(s)

Business Owners / Decision Makers

Requirements
Must have
• See attached document 'trailcrest freebie' for text to be utilized in the finished deliverable.
• See the attached image 'Site Design' for the website aesthetic.

```html
<!DOCTYPE html>
<html lang="en">
<head>
<meta charset="utf-8">
<title>Trailcrest – 10 Questions To Choose The Best Technology Advisor</title>
<link rel="stylesheet" href="https://fonts.googleapis.com/css2?family=Cinzel:wght@400;600&family=Open+Sans:ital,wght@0,300;0,400;0,600;0,700;1,400&display=swap">
<style>
:root{
  --bg:#c9c9c9;
  --slate:#37464e;
  --slate-dark:#2b373e;
  --orange:#c8743f;
  --ink:#3a3a3a;
  --paper:#ffffff;
}
*{box-sizing:border-box;margin:0;padding:0}
html,body{width:922px;height:1200px;overflow:hidden;background:var(--bg)}
body{position:relative;font-family:"Open Sans",Arial,sans-serif;color:var(--ink)}
.sheet-label{position:absolute;width:377px;text-align:center;font-size:18px;font-weight:600;color:#222;letter-spacing:.3px}
.page{position:absolute;width:377px;height:488px;background:var(--paper);overflow:hidden;box-shadow:0 1px 3px rgba(0,0,0,.25)}
.edge-strip{position:absolute;left:0;right:0;bottom:0;height:13px;background:linear-gradient(90deg,#3b3f42,#6b6f72,#3b3f42)}
.footer-band{position:absolute;left:0;right:0;display:flex;align-items:center;justify-content:center;font-family:"Cinzel",serif;font-size:9.5px;color:#fff;letter-spacing:.3px;background:linear-gradient(90deg,var(--slate) 0%,var(--slate) 45%,var(--orange) 100%)}
/* cover */
.cover-photo{position:absolute;left:203px;top:0;width:174px;height:432px;background:linear-gradient(180deg,#b9bcbc 0%,#dfe6ea 35%,#9ea3a5 70%,#cfd3d4 100%)}
.cover-brand{position:absolute;left:0;top:0;width:203px;height:152px;background:var(--paper);border-bottom-right-radius:10px;display:flex;flex-direction:column;align-items:center;justify-content:center;gap:3px}
.brand-dot{width:52px;height:52px;border-radius:50%;background:var(--orange);margin-bottom:8px}
.brand-name{font-family:"Open Sans",Arial,sans-serif;font-weight:400;font-size:17px;color:var(--slate);letter-spacing:2px}
.brand-tag{font-family:"Open Sans",Arial,sans-serif;font-weight:400;font-size:7px;color:var(--slate);letter-spacing:.4px}
.cover-title{position:absolute;left:0;top:154px;width:221px;height:131px;background:var(--slate);color:#fff;text-align:center;padding-top:14px;box-shadow:55px 0 0 var(--orange)}
.cover-title .lead{font-weight:300;font-size:13px;line-height:16px}
.cover-title hr{border:0;border-top:1px solid rgba(255,255,255,.6);width:130px;margin:6px auto 8px}
.cover-title .main{font-family:"Cinzel",serif;font-size:22px;line-height:22px}
.cover-title .main b{display:block;font-weight:600;font-size:32px;line-height:32px}
.cover-intro{position:absolute;left:0;top:285px;width:203px;height:147px;background:#f4f5f5;padding:22px 20px 0 24px;font-style:italic;font-size:6.5px;line-height:9.2px;text-align:center;color:#444}
/* questions */
.q{margin-bottom:20px}
.q-head{font-size:10px;line-height:12px;color:var(--orange);font-weight:600}
.q-head .icon{display:inline-block;width:9px;height:9px;background:var(--slate);color:#fff;font-size:7px;line-height:9px;text-align:center;margin-right:5px;vertical-align:1px}
.rule{position:relative;height:1px;background:var(--slate);margin:3px 3px 8px 0}
.rule::after{content:"";position:absolute;right:-3px;top:-2px;width:4px;height:4px;border:1px solid var(--slate);border-radius:50%;background:var(--paper)}
.q p{font-size:5.6px;line-height:7.3px;text-align:justify}
.on-dark .q-head{color:#fff}
.on-dark .q-head .icon{background:var(--orange)}
.on-dark .rule{background:#cfd5d8}
.on-dark .rule::after{border-color:#cfd5d8;background:var(--slate-dark)}
.on-dark p{color:#d6dbde}
.content{position:absolute;left:27px;right:27px}
.watermark-q{position:absolute;right:-40px;top:10px;font-family:"Cinzel",serif;font-size:300px;color:#f1f1f1;line-height:1}
/* inner 2 */
.dark-panel{position:absolute;left:0;right:0;top:246px;height:189px;background:var(--slate)}
.maze-photo{position:absolute;left:226px;top:246px;width:151px;height:226px;background:linear-gradient(180deg,#dfe3e5,#b8bec2 60%,#e9ecee)}
/* inner 3 */
.page-dark{background:radial-gradient(circle at 50% 30%,#3d4c54,var(--slate-dark))}
.contact-card{position:absolute;left:0;right:0;top:331px;height:81px;background:#f1f2f2;border-top:2px solid var(--orange);border-radius:14px 14px 0 0;display:flex;align-items:center}
.card-brand{display:flex;align-items:center;gap:8px;margin-left:27px;width:170px}
.card-brand .brand-dot{width:28px;height:28px;margin:0}
.card-brand .brand-name{font-size:12px}
.card-brand .brand-tag{font-size:5.3px}
.contact{position:relative;width:150px}
.contact h3{display:inline-block;background:var(--orange);color:#fff;font-weight:400;font-size:9px;padding:1px 10px;border-radius:8px 0 8px 0;margin-bottom:5px}
.contact li{list-style:none;font-size:6.2px;line-height:7.4px;font-weight:600;color:#333;display:flex;gap:4px;margin-bottom:1px}
.contact svg{flex:none;margin-top:1px}
</style>
</head>
<body>

<div class="sheet-label" style="left:83px;top:52px">COVER PAGE</div>
<div class="sheet-label" style="left:471px;top:52px">INNER PAGE 1</div>
<div class="sheet-label" style="left:83px;top:1116px">INNER PAGE 2</div>
<div class="sheet-label" style="left:471px;top:1116px">INNER PAGE 3</div>

<section class="page" style="left:83px;top:86px">
  <div class="cover-photo" role="img" aria-label="Photo of a businessman standing at a round window looking out over a city skyline"></div>
  <div class="cover-brand">
    <span class="brand-dot"></span>
    <span class="brand-name">TRAILCREST</span>
    <span class="brand-tag">CHART YOUR COMPANY COURSE</span>
  </div>
  <div class="cover-title">
    <div class="lead">10 Questions To<br>Choose The Best</div>
    <hr>
    <div class="main">TECHNOLOGY<b>ADVISOR</b></div>
  </div>
  <div class="cover-intro">When you choose a technology advisor whether it be a Managed Service Provider, fractional CIO or a full-time CIO you need to make sure that they understand business just as much as they understand technology. Some of the biggest complaints about the IT department are that they just don't "Get it". The questions below should help you determine whether or not they have a technology mindset or a business mindset.</div>
  <div class="footer-band" style="top:432px;height:43px">WWW.VENTURETRAILCREST-EXAMPLE.COM</div>
  <div class="edge-strip"></div>
</section>

<section class="page" style="left:471px;top:86px">
  <div class="watermark-q">Q</div>
  <div class="content" style="top:26px">
    <div class="q">
      <div class="q-head"><span class="icon">Q</span>What is scalability? How important is it from a technology perspective on a scale of 1-&gt;10 with 10 being the highest? What all does scalability impact?</div>
      <div class="rule"></div>
      <p>This question is designed to get a reading on the person's mindset. A typical technology-minded response would be something describing the ability of systems or software to scale by adding additional resources. When working from a business point of view, however, you want to see it defined as the ability for the organization to support increased volume without sacrificing margins. The importance of this concept cannot be overstated and should be a 9 or 10 in terms of ranking. Regarding impact, you want to see not just an understanding of having to spend money two or three times for a different solution to the same problem, but an acknowledgment of the 'total' cost, including adoption fatigue, the opportunity cost of change, and the competitive disadvantage it creates. For concepts of business scalability refer to 'Growing Lean' by Dale Whitcombe.</p>
    </div>
    <div class="q">
      <div class="q-head"><span class="icon">Q</span>Provide an example where you solved a problem without the use of technology.</div>
      <div class="rule"></div>
      <p>Often technology-minded individuals become so wrapped up in the solutions themselves they fail to realize a policy or process change is far more effective and simple than making changes to existing or introducing new technology. Asking for a specific example here should demonstrate the ability to think from a business mindset. For specific examples reference 'The Relay Project' by Moreau, Lind, and Haskell.</p>
    </div>
    <div class="q">
      <div class="q-head"><span class="icon">Q</span>How do you go about prioritizing solutions in order of importance for implementation / adoption?</div>
      <div class="rule"></div>
      <p>Answers here should include reference to some form of discovery process or a thorough evaluation at the operations level. One of the key skill sets for someone approaching technology from a business point of view is mapping solutions and their respective importance to business outcomes and (often more importantly) eliminating bottlenecks while respecting that some implementations must necessarily come before others to be viable. For reference on the Theory of Constraints see 'The Aim' by Aaron Feldsten.</p>
    </div>
    <div class="q">
      <div class="q-head"><span class="icon">Q</span>What is Information Technology Debt?</div>
      <div class="rule"></div>
      <p>Stated simply, 'IT Debt' is a measurement of the out-of-date, incomplete or yet-to-be-defined technology changes. Debt occurs for a number of reasons, including lack of qualified personnel to implement the needed solutions (or recognize the problem in the first place); historical spending haunting the organization "we spent money on something like this before and look what it got us"; fire-fighting (addressing issues purely reactively in a downward spiral leaving no time for fixing the real underlying problem); or most commonly, the budget being already allocated to other company endeavors that seem immediately more pressing. By recognizing what IT Debt is, the individual demonstrates an acknowledgment of how impactful it can be when neglected and not brought to the forefront of business planning sessions.</p>
    </div>
  </div>
  <div class="footer-band" style="top:452px;height:23px">WWW.VENTURETRAILCREST-EXAMPLE.COM</div>
  <div class="edge-strip"></div>
</section>

<section class="page" style="left:83px;top:603px">
  <div class="content" style="top:28px">
    <div class="q">
      <div class="q-head"><span class="icon">Q</span>Provide an example where you argued against implementing a technology solution and why.</div>
      <div class="rule"></div>
      <p>Despite it being seemingly obvious, using 'outside of budget' is not a good answer. Business-minded technology advisors should be intimately aware of how well a proposed solution will integrate into the existing company ecosystem (software tools already present, workflow, and processes), if it drives the company toward reducing/eliminating a bottleneck (and thereby creates more leverage), and if it fits the company's culture. If any of these are a no, the solution should be carefully examined for what it really offers the organization. If yes, the budget should be evaluated as a cost-benefit analysis, not a flat number 'not to exceed'.</p>
    </div>
    <div class="q">
      <div class="q-head"><span class="icon">Q</span>What is your ideal method for maintaining technology alignment for the company?</div>
      <div class="rule"></div>
      <p>You want to see a specific process envisioned here. At the very least a recommendation to be involved in business planning meetings or retreats, and ideally a standing technology focused meeting with leadership present should be argued for. For technology to be truly in alignment, it must fit the needs of the organization, not the other way around. This needs to come from the top level, and it means a representative must be present in critical business strategy meetings to understand where the company is headed, what operational constraints they are encountering, and what their short-term goals are. For an outline of how this model has been the underlying key to success for several well-known companies reference 'Steady to Strong' by Jon Callister.</p>
    </div>
  </div>
  <div class="dark-panel"></div>
  <div class="maze-photo" role="img" aria-label="Photo of a businessman with a briefcase standing at the entrance of a white maze"></div>
  <div class="content on-dark" style="top:258px;right:168px">
    <div class="q">
      <div class="q-head" style="font-size:10.5px;line-height:12.5px"><span class="icon">Q</span>How do you plan on measuring and monitoring the adoption success of a solution or project?</div>
      <div class="rule"></div>
      <p style="font-size:6px;line-height:8.9px">Technically minded individuals often look at the point of 'it's up and running and it all works', as where their responsibilities end. Someone with a business mindset should demonstrate that evaluating how well the solution has been adopted into the day to day workflow, and to what degree the solution has increased leverage or operational transparency are the true critical indicators of success. There should be a specific process of follow-up after implementation to flag adoption or workflow issues due to problems such as inadequate training, unforeseen incompatibilities (whether they be process or technology related), or simply resistance to change. These findings can then be brought back to leadership to evaluate how best to improve successful adoption going forward.</p>
    </div>
  </div>
  <div class="footer-band" style="top:435px;height:40px;background:linear-gradient(90deg,var(--slate),var(--orange) 50%,var(--slate))">WWW.VENTURETRAILCREST-EXAMPLE.COM</div>
  <div class="edge-strip"></div>
</section>

<section class="page page-dark" style="left:471px;top:603px">
  <div class="content on-dark" style="top:34px">
    <div class="q" style="margin-bottom:26px">
      <div class="q-head" style="font-size:7.6px;line-height:11px;font-weight:700"><span class="icon">Q</span>Provide an example where you had to balance customer and employee technology experience with security and compliance.</div>
      <div class="rule"></div>
      <p>A critical role fulfilled by a technology advisor is being able to balance maintaining compliance and sound security practices with as painless of a technology experience as possible. They should be able to weigh the critical importance of protecting the organization from the negative public relations and liability of a security flaw while respecting that a solution must be usable to be useful. Look for an example that demonstrates an understanding of both sides and strikes a balance without going to an extreme in either direction.</p>
    </div>
    <div class="q" style="margin-bottom:26px">
      <div class="q-head" style="font-size:7.6px;line-height:11px;font-weight:700"><span class="icon">Q</span>Can you give me an example of a time you gave a suggestion for a solution and it was not taken? Describe the solution and why it was important to the organization. And why do you think they didn't implement it?</div>
      <div class="rule"></div>
      <p>When they describe why they think the solution was important do they simply talk about risk reduction or uptime improvements without tying them back to an organizational goal or bottleneck. Being able to demonstrate actual business value is a critical skill for a technology advisor. For reference on technical excellence in service of business objectives rather than blindly servicing requirements see 'A Place at The Desk' by Martin Selwood.</p>
    </div>
    <div class="q">
      <div class="q-head" style="font-size:7.6px;line-height:11px;font-weight:700"><span class="icon">Q</span>What would you do first, if you were selected as our advisor? Can you give me details on what your discovery or on-boarding process includes?</div>
      <div class="rule"></div>
      <p>You are looking to make sure that they don't stop at the technology. There should be a higher focus on understanding what the company processes are and how the people inside the organization get work done. If they focus only on network, security, and disaster recovery assessments then they do not have a business mindset.</p>
    </div>
  </div>
  <div class="contact-card">
    <div class="card-brand">
      <span class="brand-dot"></span>
      <div><div class="brand-name">TRAILCREST</div><div class="brand-tag">CHART YOUR COMPANY COURSE</div></div>
    </div>
    <div class="contact">
      <h3>CONTACT US</h3>
      <ul>
        <li><svg width="6" height="7" viewBox="0 0 6 7"><path d="M3 0a2.4 2.4 0 0 0-2.4 2.4C.6 4.2 3 7 3 7s2.4-2.8 2.4-4.6A2.4 2.4 0 0 0 3 0z" fill="#c8743f"/><circle cx="3" cy="2.4" r=".9" fill="#fff"/></svg><span>1420 Meridian Ridge Parkway,<br>Suite 310 Brookhaven, TX 75500</span></li>
        <li><svg width="6" height="6" viewBox="0 0 6 6"><circle cx="3" cy="3" r="3" fill="#c8743f"/><rect x="1.3" y="2" width="3.4" height="2.2" fill="#fff"/></svg><span>hello@venturetrailcrest-example.com</span></li>
        <li><svg width="6" height="6" viewBox="0 0 6 6"><circle cx="3" cy="3" r="3" fill="#c8743f"/><path d="M2 1.5l.7.8-.4.5a2.5 2.5 0 0 0 .9.9l.5-.4.8.7-.5.7C2.8 4.6 1.4 3.2 1.3 2z" fill="#fff"/></svg><span>(555) 014-2290</span></li>
      </ul>
    </div>
  </div>
  <div class="footer-band" style="top:412px;height:40px;background:var(--orange)">WWW.VENTURETRAILCREST-EXAMPLE.COM</div>
  <div class="edge-strip"></div>
</section>

</body>
</html>
```